依頼詳細
■サイトマップ
①トップ
②ミナテックについて
③エアコンクリーニング
④水廻りクリーニング
⑤その他クリーニング
⑥フロアコーティング
⑦水廻りコーティング
⑧料金表
⑨実績紹介(一覧)
⑩実績紹介(詳細)
⑪お申し込みの流れ
⑫よくあるご質問
⑬お申し込み・お問い合わせ
⑭ニュース(一覧)
⑮ニュース(詳細)
⑯ブログ(一覧)
⑰ブログ(詳細)
⑱お客様の声(詳細)
⑲お客様の声(詳細)

■優先事項
1.ユーザビリティー
2.凝ったデザイン
3.編集更新

■期待する効果
1.新規顧客の獲得
2.問い合わせ数の向上
3.売上の向上

■ターゲット
【性別】男女比(女性:6.5 男性:3.5)
【年代】20代~40代
【属性】主婦 子連れ 会社員

■素材について
会社ロゴデータ ※後日提供
写真データ(人物・施術内容) ※後日提供

■SNS
LINE@ 会社用
Instagram 会社用 ※取得中

■テイスト
清潔感 優しい シンプル

■デザイン
シンプル(2) 複雑
単色  (4) カラフル
暗い  (4) 明るい
日常  (3) 高級
遊び心 (3) 厳粛
未来的 (3) 伝統的
女性  (2.5) 男性
サイトURL
ページ数
1ページ
希望イメージ
シンプル 複雑
単色 カラフル
暗い 明るい
日常 高級
遊び心 厳粛
未来的 伝統的
女性的 男性的
希望する色
水色系、緑系
納品ファイル
• イラストレーター形式 (.ai)
• フォトショップ形式 (.psd)
• PNG形式 (.png)
補足説明
素材①
サイトマップ・ワイヤーフレーム
http://filebako-demo.jp/download/a81c3e5d0b7f4426c9e2d17f08ab53c6e4f9d021
ダウンロードパスワード pass

素材②
サクモア:https://jp.sakumore-demo.com/
当社で定期契約をしています。クレジット購入のみのもの以外をご利用下さい。
また定期契約のものは弊社の負担となり、ランサー様に負担はありません。
カンプ画像を入れてください。

素材③
現行サイトより引用してください。
URL:http://kumo.hanaten-demo.net/~breeze/minatec/
URL:https://ieyoro-demo.jp/000583921/
画像やテキストに関しては一旦引き抜いて頂いて構いません。
追加で撮影した素材をアップしましたので、
ご確認の上ご使用ください。

http://filebako-demo.jp/download/c27e9a0f4d1b8e3357af6c20d9e1b4a8f05c7e19
ダウンロードパスワード pass
提案がないため延長させて頂きます!
皆様何卒よろしくお願いいたいます。
ご提案が少ないため、延長させて頂きます。
皆様、何卒よろしくお願いいたいます。

素敵なご提案をありがとうございます!

皆様ご提案ありがとうございます!

```html
<!DOCTYPE html>
<html lang="ja">
<head>
<meta charset="utf-8">
<title>ミナテック | ハウスクリーニング</title>
<link rel="stylesheet" href="https://fonts.googleapis.com/css2?family=M+PLUS+Rounded+1c:wght@400;700&family=Noto+Sans+JP:wght@400;700&display=swap">
<style>
:root{
  --blue:#3fa9d9;
  --blue-dark:#2a8cbf;
  --blue-pale:#e9f6fc;
  --blue-stripe:#dff1f9;
  --green:#5aa63c;
  --text:#444;
  --muted:#888;
  --line:#d9e6ec;
  --white:#fff;
  --footer:#f4f7f8;
}
*{box-sizing:border-box;margin:0;padding:0}
html,body{width:1200px;height:3688px;overflow:hidden}
body{font-family:"Noto Sans JP",sans-serif;color:var(--text);background:var(--white);font-size:14px;line-height:1.7}
a{color:inherit;text-decoration:none}

.topbar{height:18px;background:var(--blue);color:#fff;font-size:11px;line-height:18px;padding-left:20px;white-space:nowrap}

.header{height:126px;display:flex;align-items:center;padding:0 24px;gap:22px;white-space:nowrap}
.header > *{flex-shrink:0}
.logo{display:flex;align-items:center;gap:12px}
.logo-mark{width:54px;height:54px;border-radius:50%;background:var(--blue-pale);border:2px solid var(--blue)}
.logo-name{font-family:"M PLUS Rounded 1c",sans-serif;font-weight:700;font-size:30px;color:var(--blue-dark);white-space:nowrap}
.header-info{font-size:11px;line-height:1.8;color:var(--muted)}
.header-tel{font-family:"M PLUS Rounded 1c",sans-serif;font-weight:700;font-size:26px;color:var(--blue-dark);display:flex;align-items:center;gap:6px;margin-left:auto;white-space:nowrap}
.btn-contact{background:var(--green);color:#fff;font-weight:700;padding:10px 20px;border-radius:4px;font-size:15px;white-space:nowrap}
.sns{display:flex;gap:8px}
.sns span{width:38px;height:38px;border-radius:8px;background:var(--green)}
.sns span+span{background:#c8508a}

.nav{height:52px;background:var(--blue);display:flex}
.nav a{flex:1 1 auto;color:#fff;text-align:center;line-height:52px;font-size:14px;white-space:nowrap;padding:0 8px;border-right:1px solid rgba(255,255,255,.35)}
.nav a:last-child{border-right:0}

.hero{height:368px;position:relative;background:linear-gradient(90deg,#cfe5ef 0%,#e8f3f8 45%,#b9d8e6 100%)}
.hero-copy{position:absolute;left:70px;top:95px;font-family:"M PLUS Rounded 1c",sans-serif;font-weight:700;font-size:38px;line-height:1.7;color:var(--blue-dark)}
.hero-copy span{background:rgba(255,255,255,.85);padding:2px 10px}

.intro{height:420px;text-align:center;padding-top:52px;background:linear-gradient(180deg,#fff,#f3f9fb)}
.intro h2{font-family:"M PLUS Rounded 1c",sans-serif;font-size:28px;color:var(--blue);margin-bottom:28px}
.intro p{font-size:14px;line-height:2.2;color:var(--text)}
.btn{display:inline-block;background:var(--blue);color:#fff;font-size:14px;padding:9px 46px;border-radius:3px;margin-top:32px;white-space:nowrap}
.btn::after{content:" ›"}

.services{height:600px;padding:40px 100px 0}
.svc-big{display:flex;gap:40px;margin-bottom:24px}
.card{border:3px solid var(--blue);border-radius:8px;background:#fff;overflow:hidden}
.card-big{flex:1;height:290px;display:flex}
.card-big .txt{width:45%;padding:22px 20px}
.card-big h3{font-family:"M PLUS Rounded 1c",sans-serif;font-size:26px;color:var(--blue);line-height:1.3;margin-bottom:16px}
.card-big p{font-size:12px;line-height:1.9}
.card-big .ph{flex:1}
.svc-small{display:flex;gap:32px}
.card-small{flex:1;height:190px;position:relative}
.card-small .ph{height:100%}
.card-small .label{position:absolute;left:0;right:0;bottom:0;background:rgba(255,255,255,.92);text-align:center;font-family:"M PLUS Rounded 1c",sans-serif;font-weight:700;color:var(--blue);font-size:17px;padding:8px 0}
.ph-air{background:linear-gradient(135deg,#f5f7f8,#cfd9de)}
.ph-water{background:linear-gradient(135deg,#e8eef1,#9fb3bd)}
.ph-floor{background:linear-gradient(135deg,#e8c79a,#b9895a)}
.ph-sink{background:linear-gradient(135deg,#eef2f4,#b5c3c9)}
.ph-room{background:linear-gradient(135deg,#f2efe9,#c9c0b3)}

.flow{height:520px;background:repeating-linear-gradient(90deg,var(--blue-pale) 0 14px,var(--blue-stripe) 14px 28px);text-align:center;padding-top:44px}
.sec-title{font-family:"M PLUS Rounded 1c",sans-serif;font-weight:700;font-size:24px;color:#333}
.steps{display:flex;justify-content:center;align-items:center;gap:26px;margin-top:40px}
.step{width:170px}
.step-no{font-family:"M PLUS Rounded 1c",sans-serif;font-size:28px;color:var(--blue);letter-spacing:2px}
.step-circle{width:150px;height:150px;border-radius:50%;background:#fff;margin:8px auto 12px;display:flex;align-items:center;justify-content:center}
.step-label{font-size:15px;font-weight:700}
.arrow{width:44px;height:44px;border-radius:50%;background:#fff;display:flex;align-items:center;justify-content:center;margin-top:10px}
.btn-green{display:inline-block;background:var(--green);color:#fff;font-weight:700;padding:14px 110px;margin-top:38px;font-size:16px;white-space:nowrap}

.works{height:420px;text-align:center;padding-top:44px}
.work-list{display:flex;justify-content:center;gap:36px;margin-top:28px}
.work{width:260px;text-align:left}
.work .ph{height:160px}
.work time{display:block;text-align:center;font-size:13px;color:var(--muted);margin-top:6px}
.work p{font-size:13px;text-align:center}
.ph-w1{background:linear-gradient(135deg,#3b4a58,#8fa3b3)}
.ph-w2{background:linear-gradient(135deg,#1f2428,#7a8188)}
.ph-w3{background:linear-gradient(135deg,#2a6aa8,#9db8cc)}

.news-blog{height:440px;display:flex;justify-content:center;gap:80px;padding-top:50px;border-top:1px solid var(--line)}
.column{width:440px;text-align:center}
.column h2{font-family:"M PLUS Rounded 1c",sans-serif;font-size:30px;color:#333;letter-spacing:2px;margin-bottom:18px}
.column ul{list-style:none;text-align:left}
.column li{display:flex;gap:28px;border-bottom:1px dotted #ccc;padding:10px 4px;font-size:13px;white-space:nowrap}
.column li time{color:var(--muted)}

.campaign{height:320px;display:flex;justify-content:center;align-items:center}
.camp-box{width:640px;height:260px;border:3px solid var(--blue);background:var(--blue-pale);position:relative;padding:28px 30px}
.camp-box h2{font-family:"M PLUS Rounded 1c",sans-serif;font-size:32px;color:#e9863a;line-height:1.3}
.camp-box .sub{font-family:"M PLUS Rounded 1c",sans-serif;font-weight:700;font-size:22px;color:var(--blue-dark);margin-top:12px}
.camp-box .sub em{font-style:normal;color:#e45656;font-size:28px}
.camp-box .btn{margin-top:18px}
.camp-figure{position:absolute;right:20px;top:20px;width:190px;height:220px;border-radius:8px;background:linear-gradient(180deg,#cfeaf6,#8ccbe6)}

.footer{height:320px;background:var(--footer);display:flex;padding:40px 90px 0;gap:90px}
.footer .logo-name{font-size:28px}
.footer .logo-mark{width:46px;height:46px}
.f-info{font-size:12px;line-height:2;margin-top:14px;white-space:nowrap}
.f-tel{font-family:"M PLUS Rounded 1c",sans-serif;font-weight:700;font-size:28px;color:var(--blue-dark);display:flex;align-items:center;gap:8px;white-space:nowrap}
.f-col h4{font-size:13px;margin-bottom:10px}
.f-col ul{list-style:none;font-size:12px;line-height:2.1;white-space:nowrap}
.f-col li::before{content:"› ";color:var(--blue)}
.copy{height:28px;background:var(--blue);color:#fff;text-align:center;font-size:11px;line-height:28px}
</style>
</head>
<body>
<div class="topbar">大阪市の地域密着ハウスクリーニング専門店ミナテック</div>

<header class="header">
  <div class="logo"><span class="logo-mark"></span><span class="logo-name">ミナテック</span></div>
  <div class="header-info">営業時間 09:00〜19:00<br>定休日 年中無休</div>
  <div class="header-info">〒530-0000 大阪府大阪市青葉区<br>みどり町2-14-5</div>
  <div class="header-tel">
    <svg width="24" height="24" viewBox="0 0 24 24"><path fill="#2a8cbf" d="M6.6 10.8a15 15 0 0 0 6.6 6.6l2.2-2.2c.3-.3.7-.4 1-.2 1.1.4 2.3.6 3.6.6.6 0 1 .4 1 1V20c0 .6-.4 1-1 1C10.6 21 3 13.4 3 4c0-.6.4-1 1-1h3.5c.6 0 1 .4 1 1 0 1.3.2 2.5.6 3.6.1.3 0 .7-.2 1z"/></svg>
    050-6218-4073
  </div>
  <a class="btn-contact" href="#">お問い合わせ</a>
  <div class="sns"><span></span><span></span></div>
</header>

<nav class="nav">
  <a href="#">トップ</a><a href="#">ミナテックについて</a><a href="#">料金表</a><a href="#">実績紹介</a><a href="#">お申し込みの流れ</a><a href="#">よくある質問</a><a href="#">お申し込み・お問い合わせ</a>
</nav>

<section class="hero" role="img" aria-label="エアコンを洗浄するスタッフの写真">
  <p class="hero-copy"><span>丁寧な作業、丁寧な対応を</span><br><span>心がけております！</span></p>
</section>

<section class="intro">
  <h2>熟練されたスキルを持ったプロが隅々まで洗浄致します！</h2>
  <p>当店の作業は、すべて経験豊富なスタッフが担当します。<br>エアコンや水廻りなど、ご家庭の汚れを丁寧に落とします。<br>小さなお子様がいるご家庭にも安心の洗剤を使用しています。<br>まずはお気軽にお問い合わせください。</p>
  <a class="btn" href="#">ミナテックについて</a>
</section>

<section class="services">
  <div class="svc-big">
    <div class="card card-big">
      <div class="txt"><h3>エアコン<br>クリーニング</h3><p>分解洗浄で内部のカビや汚れを除去。<br>嫌なニオイもすっきり解消します。<br>家庭用から業務用まで対応可能。</p></div>
      <div class="ph ph-air" role="img" aria-label="壁掛けエアコンの写真"></div>
    </div>
    <div class="card card-big">
      <div class="txt"><h3>水廻り<br>クリーニング</h3><p>キッチンや浴室の頑固な汚れを除去。<br>水垢やカビも丁寧に落とします。<br>トイレ・洗面所もおまかせください。</p></div>
      <div class="ph ph-water" role="img" aria-label="キッチンの写真"></div>
    </div>
  </div>
  <div class="svc-small">
    <div class="card card-small"><div class="ph ph-floor" role="img" aria-label="フローリングの部屋の写真"></div><div class="label">フロアコーティング</div></div>
    <div class="card card-small"><div class="ph ph-sink" role="img" aria-label="洗面台の写真"></div><div class="label">水廻りコーティング</div></div>
    <div class="card card-small"><div class="ph ph-room" role="img" aria-label="明るいリビングの写真"></div><div class="label">その他クリーニング</div></div>
  </div>
</section>

<section class="flow">
  <h2 class="sec-title">お申し込みの流れ</h2>
  <div class="steps">
    <div class="step"><div class="step-no">STEP1</div><div class="step-circle"><svg width="56" height="56" viewBox="0 0 24 24" fill="none" stroke="#3fa9d9" stroke-width="1.6"><rect x="7" y="2" width="10" height="20" rx="2"/><circle cx="12" cy="18.5" r=".8" fill="#3fa9d9"/></svg></div><div class="step-label">ネット予約</div></div>
    <div class="arrow"><svg width="16" height="16" viewBox="0 0 24 24" fill="none" stroke="#3fa9d9" stroke-width="3"><path d="M9 5l7 7-7 7"/></svg></div>
    <div class="step"><div class="step-no">STEP2</div><div class="step-circle"><svg width="60" height="60" viewBox="0 0 24 24" fill="none" stroke="#3fa9d9" stroke-width="1.6"><rect x="3" y="4" width="18" height="12" rx="1"/><path d="M9 20h6M12 16v4"/></svg></div><div class="step-label">予約確認</div></div>
    <div class="arrow"><svg width="16" height="16" viewBox="0 0 24 24" fill="none" stroke="#3fa9d9" stroke-width="3"><path d="M9 5l7 7-7 7"/></svg></div>
    <div class="step"><div class="step-no">STEP3</div><div class="step-circle"><svg width="58" height="58" viewBox="0 0 24 24" fill="none" stroke="#3fa9d9" stroke-width="1.6"><path d="M4 20l9-9M14 4a4 4 0 0 0 5 5l-3 3-5-5z"/><path d="M5 4l15 15"/></svg></div><div class="step-label">作業</div></div>
    <div class="arrow"><svg width="16" height="16" viewBox="0 0 24 24" fill="none" stroke="#3fa9d9" stroke-width="3"><path d="M9 5l7 7-7 7"/></svg></div>
    <div class="step"><div class="step-no">STEP4</div><div class="step-circle"><svg width="58" height="58" viewBox="0 0 24 24" fill="none" stroke="#3fa9d9" stroke-width="1.6"><circle cx="14" cy="9" r="5"/><path d="M14 6.5v5M12 9h4M2 18c3-2 6-2 9 0l6-2"/></svg></div><div class="step-label">お支払い</div></div>
  </div>
  <a class="btn-green" href="#">お申し込み・お問い合わせ</a>
</section>

<section class="works">
  <h2 class="sec-title">実績紹介</h2>
  <div class="work-list">
    <div class="work"><div class="ph ph-w1" role="img" aria-label="分解したエアコン部品の写真"></div><time>2018.12.08</time><p>二層式エアコンの分解洗浄</p></div>
    <div class="work"><div class="ph ph-w2" role="img" aria-label="業務用エアコンの写真"></div><time>2018.12.08</time><p>業務用エアコン天井埋込型洗浄</p></div>
    <div class="work"><div class="ph ph-w3" role="img" aria-label="洗浄作業中のエアコンの写真"></div><time>2018.12.08</time><p>ご自宅エアコンの洗浄</p></div>
  </div>
  <a class="btn" href="#">一覧はこちら</a>
</section>

<section class="news-blog">
  <div class="column">
    <h2>NEWS</h2>
    <ul>
      <li><time>2018.12.08</time>タイトルが入ります。タイトルが入ります。</li>
      <li><time>2018.12.08</time>タイトルが入ります。タイトルが入ります。</li>
      <li><time>2018.12.08</time>タイトルが入ります。タイトルが入ります。</li>
    </ul>
    <a class="btn" href="#">一覧はこちら</a>
  </div>
  <div class="column">
    <h2>BLOG</h2>
    <ul>
      <li><time>2018.12.08</time>タイトルが入ります。タイトルが入ります。</li>
      <li><time>2018.12.08</time>タイトルが入ります。タイトルが入ります。</li>
      <li><time>2018.12.08</time>タイトルが入ります。タイトルが入ります。</li>
    </ul>
    <a class="btn" href="#">一覧はこちら</a>
  </div>
</section>

<section class="campaign">
  <div class="camp-box">
    <h2>エアコンクリーニング<br>キャンペーン</h2>
    <p class="sub">2台目以降はさらに<em>500円引き</em>！</p>
    <a class="btn" href="#">詳しくはこちら</a>
    <div class="camp-figure" role="img" aria-label="作業着姿のスタッフのイラストとエアコン"></div>
  </div>
</section>

<footer class="footer">
  <div>
    <div class="logo"><span class="logo-mark"></span><span class="logo-name">ミナテック</span></div>
    <p class="f-info">〒530-0000 大阪府大阪市青葉区みどり町2-14-5<br>営業時間 09:00〜19:00 定休日 年中無休</p>
    <div class="f-tel"><svg width="24" height="24" viewBox="0 0 24 24"><path fill="#2a8cbf" d="M6.6 10.8a15 15 0 0 0 6.6 6.6l2.2-2.2c.3-.3.7-.4 1-.2 1.1.4 2.3.6 3.6.6.6 0 1 .4 1 1V20c0 .6-.4 1-1 1C10.6 21 3 13.4 3 4c0-.6.4-1 1-1h3.5c.6 0 1 .4 1 1 0 1.3.2 2.5.6 3.6.1.3 0 .7-.2 1z"/></svg>050-6218-4073</div>
  </div>
  <div class="f-col"><h4>会社案内</h4><ul><li>トップ</li><li>ミナテックについて</li><li>料金表</li><li>実績紹介</li><li>お客様の声</li></ul></div>
  <div class="f-col"><h4>&nbsp;</h4><ul><li>ニュース</li><li>ブログ</li><li>お申し込みの流れ</li><li>よくあるご質問</li><li>お申し込み・お問い合わせ</li></ul></div>
  <div class="f-col"><h4>業務案内</h4><ul><li>エアコンクリーニング</li><li>水廻りクリーニング</li><li>その他クリーニング</li><li>フロアコーティング</li><li>水廻りコーティング</li></ul></div>
</footer>
<div class="copy">Copyright 2018 ミナテック All Rights Reserved.</div>
</body>
</html>
```